Acupuncture Medspa needs a business card design

I need a business card design that looks professional, has a spa-like quality and can offer a promo on the back. Initial promo is "First session free". The tagline of NeedleNook is: Refresh, Restore, Rejuvenate.

NeedleNook is a membership-based acupuncture medspa that offers acupuncture, cupping, and herbal therapies. Members choose between the "Refresh" membership which is for stress relief, or "Restore" which is for treating health conditions, and lastly "Rejuvenate" which is for natural facial enhancement.

Industry/Entity Type

Health And Wellness

Contact Information for Business Card

Coral Haskins, MAC, L.Ac.
612-555-0193
www.needlenook-example.com

Font styles to use
Serif
Sans Serif

Colors

Designer to choose colors to be used in the design.

Requirements
Must have
• The project must have NeedleNook logo, promo on the back, and contact information
Nice to have
• I would like to see the colors of the logo used.

```html
<!DOCTYPE html>
<html lang="en">
<head>
<meta charset="utf-8">
<title>NeedleNook business card</title>
<link href="https://fonts.googleapis.com/css2?family=Montserrat:wght@600&family=Lato:wght@400;700&display=swap" rel="stylesheet">
<style>
  :root {
    --teal: #0b8a84;
    --brown: #3a2219;
    --white: #ffffff;
    --ink: #2b2b2b;
    --backdrop: #e9e9e9;
  }
  * { box-sizing: border-box; margin: 0; padding: 0; }
  html, body { width: 1200px; height: 895px; overflow: hidden; }
  body {
    background: var(--backdrop);
    display: flex;
    flex-direction: column;
    align-items: center;
    justify-content: center;
    gap: 40px;
    font-family: "Lato", sans-serif;
  }
  .card {
    position: relative;
    width: 620px;
    height: 354px;
    border-radius: 22px;
    background: var(--white);
    overflow: hidden;
    box-shadow: 0 6px 18px rgba(0,0,0,0.12);
  }
  /* Front */
  .card-front {
    display: flex;
    flex-direction: column;
    align-items: center;
    justify-content: center;
    gap: 34px;
  }
  .brand-name {
    font-family: "Montserrat", sans-serif;
    font-weight: 600;
    font-size: 58px;
    letter-spacing: 3px;
    color: var(--teal);
    text-transform: uppercase;
  }
  .tagline {
    font-size: 19px;
    letter-spacing: 2.5px;
    color: var(--ink);
  }
  /* Back */
  .back-art { position: absolute; inset: 0; }
  .contact {
    position: absolute;
    right: 30px;
    top: 122px;
    text-align: right;
    color: var(--white);
  }
  .person-name {
    font-weight: 700;
    font-size: 28px;
    color: var(--brown);
    line-height: 1.1;
  }
  .credentials { font-size: 15px; margin-bottom: 12px; }
  .contact-line {
    display: flex;
    justify-content: flex-end;
    align-items: center;
    gap: 9px;
    font-size: 15px;
    line-height: 1.55;
  }
  .contact-line svg { width: 13px; height: 13px; flex: none; }
  .promo {
    position: absolute;
    left: 34px;
    bottom: 28px;
    font-size: 22px;
    color: var(--white);
  }
  .promo strong { font-weight: 700; font-size: 27px; color: var(--brown); }
</style>
</head>
<body>

<section class="card card-front">
  <h1 class="brand-name">NeedleNook</h1>
  <p class="tagline">Refresh, Restore, Rejuvenate</p>
</section>

<section class="card card-back">
  <svg class="back-art" viewBox="0 0 620 354" width="620" height="354" aria-hidden="true">
    <path class="swoosh-brown" d="M262,212 C300,120 400,22 620,12 L620,30 C430,40 335,105 282,196 Z" fill="var(--brown)"/>
    <path class="wave-teal" d="M0,262 C150,300 250,280 300,180 C340,100 430,50 620,45 L620,354 L0,354 Z" fill="var(--teal)"/>
    <path class="arc-teal" d="M60,225 C150,258 230,262 290,236 C230,252 150,252 60,232 Z" fill="var(--teal)"/>
    <circle class="mark-circle" cx="160" cy="125" r="72" fill="none" stroke="var(--teal)" stroke-width="4"/>
  </svg>

  <div class="contact">
    <p class="person-name">Coral Haskins</p>
    <p class="credentials">MAC, L.Ac.</p>
    <p class="contact-line">612-555-0193
      <svg viewBox="0 0 14 14"><rect x="3" y="1" width="8" height="12" rx="1.5" fill="none" stroke="var(--brown)" stroke-width="1.5"/></svg>
    </p>
    <p class="contact-line">coral@needlenook-example.com
      <svg viewBox="0 0 14 14"><rect x="1" y="3" width="12" height="8" fill="var(--brown)"/><path d="M1,3 L7,8 L13,3" fill="none" stroke="var(--teal)" stroke-width="1"/></svg>
    </p>
    <p class="contact-line">www.needlenook-example.com
      <svg viewBox="0 0 14 14"><circle cx="7" cy="7" r="5.5" fill="none" stroke="var(--brown)" stroke-width="1.4"/><path d="M1.5,7 H12.5 M7,1.5 V12.5" stroke="var(--brown)" stroke-width="1.1"/></svg>
    </p>
  </div>

  <p class="promo">first session <strong>free</strong></p>
</section>

</body>
</html>
```